Brimovex business card

Based on company logo and website given , to design a business card temple. Slogan "Your furry friends deserves the best"
Color style please refer to our website

```html
<!DOCTYPE html>
<html lang="en">
<head>
<meta charset="utf-8">
<title>Brimovex business card</title>
<link href="https://fonts.googleapis.com/css2?family=Arimo:wght@400;700&display=swap" rel="stylesheet">
<style>
  :root {
    --stage: #e6e6e4;
    --card: #2d2d2d;
    --card-deep: #232323;
    --brand-blue: #2470c2;
    --edge-blue: #1b4f8f;
    --ink-light: #ececec;
    --rule: #8a8a8a;
    --silver: #d9d9d9;
  }
  * { box-sizing: border-box; margin: 0; padding: 0; }
  html, body { width: 1200px; height: 801px; overflow: hidden; }
  body {
    background: var(--stage);
    font-family: "Arimo", Arial, sans-serif;
    position: relative;
  }
  .card {
    position: absolute;
    top: 240px;
    width: 540px;
    height: 310px;
    background: linear-gradient(160deg, var(--card) 0%, var(--card-deep) 100%);
    border-bottom: 4px solid var(--edge-blue);
    border-left: 2px solid var(--edge-blue);
    box-shadow: 0 12px 30px rgba(0,0,0,0.25);
    overflow: hidden;
  }
  .card--front { left: 45px; }
  .card--back { left: 615px; }

  /* front */
  .wordmark {
    font-weight: 700;
    color: var(--brand-blue);
    letter-spacing: 0.5px;
  }
  .card--front .wordmark {
    position: absolute;
    left: 60px; top: 70px;
    font-size: 50px;
  }
  .identity {
    position: absolute;
    left: 60px; top: 160px;
  }
  .identity__name {
    font-size: 22px;
    font-weight: 700;
    color: var(--brand-blue);
  }
  .identity__role {
    margin-top: 4px;
    font-size: 15px;
    color: var(--ink-light);
    text-align: right;
  }
  .divider {
    position: absolute;
    left: 275px; top: 120px;
    width: 1px; height: 100px;
    background: var(--rule);
  }
  .contacts {
    position: absolute;
    left: 295px; top: 122px;
    list-style: none;
  }
  .contacts li {
    display: flex;
    align-items: center;
    gap: 8px;
    font-size: 14px;
    color: var(--ink-light);
    margin-bottom: 10px;
  }
  .contacts svg { width: 14px; height: 14px; flex: none; }
  .contacts .accent { color: var(--brand-blue); }
  .address {
    position: absolute;
    left: 60px; bottom: 34px;
    font-size: 14px;
    color: var(--ink-light);
  }

  /* back */
  .card--back .wordmark {
    position: absolute;
    left: 34px; top: 96px;
    font-size: 54px;
    color: var(--silver);
  }
  .slogan {
    position: absolute;
    left: 36px; top: 164px;
    font-size: 17px;
    color: var(--brand-blue);
  }
  .mascot-area {
    position: absolute;
    right: 0; top: 0;
    width: 220px; height: 100%;
    background: linear-gradient(180deg, rgba(36,112,194,0.55) 0%, rgba(30,90,160,0.8) 100%);
  }
</style>
</head>
<body>
  <section class="card card--front" aria-label="Business card front">
    <div class="wordmark">Brimovex</div>
    <div class="identity">
      <p class="identity__name">Daniel Hart</p>
      <p class="identity__role">Manager</p>
    </div>
    <div class="divider"></div>
    <ul class="contacts">
      <li>
        <svg viewBox="0 0 14 14" aria-hidden="true"><circle cx="7" cy="7" r="7" fill="var(--brand-blue)"/><path d="M4.5 4 L6 4 L6.5 6 L5.6 6.6 Q6.4 8.2 7.8 8.8 L8.4 8 L10 8.5 L10 10 Q6 10.5 4 5.5 Z" fill="#fff"/></svg>
        555-014-2739
      </li>
      <li>
        <svg viewBox="0 0 14 14" aria-hidden="true"><rect x="1" y="3" width="12" height="8" fill="var(--brand-blue)"/><path d="M1 3 L7 8 L13 3" stroke="#fff" stroke-width="1" fill="none"/></svg>
        hello@brimovex-mail.com
      </li>
      <li>
        <svg viewBox="0 0 14 14" aria-hidden="true"><circle cx="7" cy="7" r="6" fill="var(--brand-blue)"/><circle cx="7" cy="7" r="4" fill="none" stroke="#fff" stroke-width="0.8"/><path d="M3 7 H11 M7 3 V11" stroke="#fff" stroke-width="0.8"/></svg>
        <span>www.<span class="accent">brimovexpets</span>.com</span>
      </li>
    </ul>
    <p class="address">Your address, city, state, ZIP 0000</p>
  </section>

  <section class="card card--back" aria-label="Business card back">
    <div class="mascot-area" role="img" aria-label="Large blue outline illustration of a seated dog"></div>
    <div class="wordmark">Brimovex</div>
    <p class="slogan">Your furry friends deserves the best</p>
  </section>
</body>
</html>
```